Trifold Pamphlet/leaflet design for Tide Nest Retreats, Trainings and Community

We would like to create a trifold leaflet showcasing Tide Nest and our retreats for promotional purposes. Tide Nest is an Australian based global company offering life-changing retreats, online trainings and inspired community within the health, wellness, personal development and human potential space.
We will use the 6 pages to showcase the Front cover with logo and tagline/keywords - Explore, Play, Connect,
Back Cover can have contact details, website , social media etc and the other 4 pages to detail
1. who Tide Nest is, what we are about, pics of the team
2. Our retreats including pictures of the Retreat Centre
3. Our Online Trainings
4 Our Inspired Community.
Each page to include text and images that I will provide shortly. Look is to align with colour palate and feel of logo and website - preview of website, in progress, here - https://kimpagecraft.sampleeditorhub.com/site/7a2c9e14/?preview=true&insitepreview=true
Little less black in the leaflets than on the website perhaps
Text is to be in poppins font.
Please advise of any questions, will forward images and text early next week - awaiting our photographer!
Best, Ned
Target Market(s)
35-55, senior leaders, business owners. 65% female, 35% male. Interested in yoga, wellbeing, peak performance, mindfulness.
Industry/Entity Type
Health And Wellness
Look and feel

```html
<!DOCTYPE html>
<html lang="en">
<head>
<meta charset="utf-8">
<title>Tide Nest Trifold Leaflet</title>
<link rel="stylesheet" href="https://fonts.googleapis.com/css2?family=Montserrat:wght@300;400;500;600;700;800&display=swap">
<style>
:root{
  --forest:#0b4a3d;
  --forest-deep:#083c31;
  --teal:#2aa38c;
  --teal-soft:#9fd3c7;
  --paper:#f4f5f4;
  --ink:#16302a;
  --ink-soft:#3c4f4a;
  --stage:#5d6166;
}
*{box-sizing:border-box;margin:0;padding:0}
html,body{width:1200px;height:1200px;overflow:hidden}
body{background:var(--stage);font-family:"Montserrat",sans-serif;color:var(--ink);position:relative}
.sheet{position:absolute;left:40px;width:1120px;height:540px;box-shadow:0 14px 30px rgba(0,0,0,.35)}
.sheet--outside{top:30px}
.sheet--inside{top:630px}
.sheet-art{position:absolute;inset:0;width:100%;height:100%}
.panel{position:absolute;top:0;width:373px;height:540px}
.panel--1{left:0}.panel--2{left:373px}.panel--3{left:746px}

.tag{display:inline-block;background:var(--teal);color:#fff;padding:1px 6px;margin-right:4px}
.heading{font-weight:800;font-size:21px;color:var(--forest);line-height:1.1}

/* outside: training menu */
.menu-title{position:absolute;top:22px;left:30px;font-weight:700;font-style:italic;font-size:20px;color:var(--forest)}
.menu-item{position:absolute;left:40px;width:293px;text-align:center}
.menu-icon{width:34px;height:34px;margin:0 auto 4px;display:block}
.pill{display:inline-block;background:var(--teal);color:#fff;font-size:11px;font-weight:600;font-style:italic;padding:2px 12px;border-radius:10px}
.menu-copy{font-size:10px;font-style:italic;color:var(--ink-soft);margin-top:5px;line-height:1.35}

/* brand name */
.brand{position:absolute;left:0;width:373px;text-align:center;font-weight:300;color:#fff;letter-spacing:.18em}
.brand--contact{top:46px;font-size:26px}
.brand--cover{top:52px;font-size:34px}

.contact-title{position:absolute;top:118px;width:373px;text-align:center;color:#fff;font-weight:700;font-size:16px;letter-spacing:.08em}
.contact-rule{position:absolute;top:146px;left:126px;width:120px;height:2px;background:var(--teal)}
.contact-line{position:absolute;left:0;width:373px;text-align:center;color:#fff}
.contact-icon{width:18px;height:18px;margin:0 auto 5px;display:block}
.contact-line--phone{top:166px;font-size:18px;font-weight:500;letter-spacing:.06em}
.contact-line--mail{top:222px;font-size:12px}
.contact-line--web{top:272px;font-size:10.5px}

.cover-head{position:absolute;top:120px;left:30px;width:313px;text-align:center;color:#fff;font-weight:800;font-size:25px;line-height:1.05;text-transform:uppercase}
.cover-sub{position:absolute;top:236px;left:40px;width:293px;text-align:center;color:#fff;font-size:11px;line-height:1.35}
.cover-rule{position:absolute;top:296px;left:126px;width:120px;height:2px;background:var(--teal)}
.cover-keys{position:absolute;top:316px;width:373px;text-align:center;color:#fff;font-weight:700;font-size:19px}

/* inside */
.section-title{position:absolute;top:30px;left:28px}
.body-copy{font-size:10.5px;line-height:1.35;color:var(--ink-soft);text-align:justify}
.who-copy{position:absolute;top:72px;left:28px;width:317px}
.with-title{position:absolute;top:24px;left:22px;width:160px;text-align:right}
.with-copy{position:absolute;top:128px;left:40px;width:142px;text-align:right;font-size:10.5px;line-height:1.3;color:var(--ink-soft)}
.why-title{position:absolute;top:24px;left:26px}
.why-copy{position:absolute;left:26px;width:321px}
.why-copy--a{top:62px}.why-copy--b{top:150px}
.brand-mark{position:absolute;top:232px;left:136px;width:100px;height:100px;border:3px solid var(--teal-soft);border-radius:50%}

.band-title{position:absolute;top:332px;left:373px;width:560px;text-align:left;padding-left:60px;color:#fff;font-weight:700;font-size:18px}
.step{position:absolute;display:flex;gap:12px;width:300px}
.step-icon{flex:0 0 36px;height:36px;border-radius:50%;background:var(--teal);display:flex;align-items:center;justify-content:center}
.step-icon svg{width:20px;height:20px}
.step-name{color:#fff;font-weight:700;font-size:13px;margin-bottom:2px}
.step-copy{color:#e6efec;font-size:10.5px;line-height:1.3}
</style>
</head>
<body>

<!-- OUTSIDE -->
<section class="sheet sheet--outside">
  <svg class="sheet-art" viewBox="0 0 1120 540" preserveAspectRatio="none">
    <defs>
      <linearGradient id="beachSky" x1="0" y1="0" x2="0" y2="1"><stop offset="0" stop-color="#c9d3da"/><stop offset=".6" stop-color="#a8b5bd"/><stop offset="1" stop-color="#8d8577"/></linearGradient>
      <linearGradient id="lakeShade" x1="0" y1="0" x2="1" y2="1"><stop offset="0" stop-color="#5b7c8e"/><stop offset=".6" stop-color="#9fb3bd"/><stop offset="1" stop-color="#d8d2c6"/></linearGradient>
      <linearGradient id="meadow" x1="0" y1="0" x2="0" y2="1"><stop offset="0" stop-color="#a7cf6a"/><stop offset="1" stop-color="#5f9a3a"/></linearGradient>
    </defs>
    <rect x="0" y="0" width="373" height="540" fill="var(--paper)"/>
    <rect x="373" y="0" width="747" height="540" fill="var(--forest)"/>
    <path d="M0,356 Q186,326 373,366 Q560,396 746,356 Q933,326 1120,376 L1120,394 Q933,344 746,374 Q560,414 373,384 Q186,344 0,374Z" fill="var(--teal)"/>
    <g role="img" aria-label="Photo: woman with arms outstretched on a beach"><path d="M0,374 Q186,344 373,384 L373,540 L0,540Z" fill="url(#beachSky)"/></g>
    <g role="img" aria-label="Photo: man relaxing in a hammock by a lake"><path d="M373,384 Q560,414 746,374 L746,540 L373,540Z" fill="url(#lakeShade)"/></g>
    <g role="img" aria-label="Photo: smiling woman lying in a sunny meadow"><path d="M746,374 Q933,344 1120,394 L1120,540 L746,540Z" fill="url(#meadow)"/></g>
    <line x1="373" y1="0" x2="373" y2="540" stroke="rgba(0,0,0,.12)"/>
    <line x1="746" y1="0" x2="746" y2="540" stroke="rgba(0,0,0,.12)"/>
  </svg>

  <div class="panel panel--1">
    <h2 class="menu-title"><span class="tag">Your</span>Training Menu</h2>
    <div class="menu-item" style="top:70px">
      <svg class="menu-icon" viewBox="0 0 34 34" fill="none" stroke="var(--teal-soft)" stroke-width="2"><rect x="7" y="15" width="20" height="15" rx="2"/><path d="M11,15 V10 a6,6 0 0 1 12,0"/></svg>
      <span class="pill">Title 1</span>
      <p class="menu-copy">Our support team is here to ensure that things run smoothly, so you can focus elsewhere.</p>
    </div>
    <div class="menu-item" style="top:162px">
      <svg class="menu-icon" viewBox="0 0 34 34" fill="none" stroke="var(--teal-soft)" stroke-width="2"><rect x="3" y="5" width="17" height="13" rx="2"/><rect x="14" y="14" width="17" height="13" rx="2"/></svg>
      <span class="pill">Title 2</span>
      <p class="menu-copy">Our support team is here to ensure that things run smoothly, so you can focus elsewhere.</p>
    </div>
    <div class="menu-item" style="top:254px">
      <svg class="menu-icon" viewBox="0 0 34 34" fill="none" stroke="var(--teal-soft)" stroke-width="2"><circle cx="17" cy="14" r="9"/><path d="M12,24 L10,31 M22,24 L24,31"/></svg>
      <span class="pill">Title 3</span>
      <p class="menu-copy">Our support team is here to ensure that things run smoothly, so you can focus elsewhere.</p>
    </div>
  </div>

  <div class="panel panel--2">
    <p class="brand brand--contact">TIDE NEST</p>
    <h2 class="contact-title">CONTACT DETAILS</h2>
    <div class="contact-rule"></div>
    <p class="contact-line contact-line--phone">
      <svg class="contact-icon" viewBox="0 0 18 18"><circle cx="9" cy="9" r="9" fill="var(--teal)"/><path d="M6,5 l2,0 l1,2.5 l-1.2,1 a6,6 0 0 0 2.7,2.7 l1,-1.2 l2.5,1 l0,2 a1,1 0 0 1 -1,1 a8,8 0 0 1 -8,-8 a1,1 0 0 1 1,-1z" fill="#fff"/></svg>
      0198 765 432</p>
    <p class="contact-line contact-line--mail">
      <svg class="contact-icon" viewBox="0 0 18 18"><circle cx="9" cy="9" r="9" fill="var(--teal)"/><rect x="4.5" y="6" width="9" height="6.5" fill="none" stroke="#fff" stroke-width="1.2"/><path d="M4.5,6 L9,9.6 L13.5,6" fill="none" stroke="#fff" stroke-width="1.2"/></svg>
      hello@tidenestmail.com</p>
    <p class="contact-line contact-line--web">
      <svg class="contact-icon" viewBox="0 0 18 18"><circle cx="9" cy="9" r="9" fill="var(--teal)"/><circle cx="9" cy="9" r="4.5" fill="none" stroke="#fff" stroke-width="1.2"/><path d="M4.5,9 H13.5 M9,4.5 V13.5" stroke="#fff" stroke-width="1.2"/></svg>
      kimpagecraft.sampleeditorhub.com</p>
  </div>

  <div class="panel panel--3">
    <p class="brand brand--cover">TIDE NEST</p>
    <h1 class="cover-head">Facilitating flow for whole human thriving</h1>
    <p class="cover-sub">Life-changing retreats, online trainings and inspired community for personal and organizational peak performance and wellbeing.</p>
    <div class="cover-rule"></div>
    <p class="cover-keys">Explore, Play, Connect,</p>
  </div>
</section>

<!-- INSIDE -->
<section class="sheet sheet--inside">
  <svg class="sheet-art" viewBox="0 0 1120 540" preserveAspectRatio="none">
    <defs>
      <linearGradient id="sofaRoom" x1="0" y1="0" x2="0" y2="1"><stop offset="0" stop-color="#e9ecee"/><stop offset=".5" stop-color="#b9c3cc"/><stop offset="1" stop-color="#4d6a8a"/></linearGradient>
      <linearGradient id="sunsetSea" x1="0" y1="0" x2="0" y2="1"><stop offset="0" stop-color="#a5a7c9"/><stop offset=".45" stop-color="#f0b46a"/><stop offset=".7" stop-color="#7b7fa3"/><stop offset="1" stop-color="#3d4670"/></linearGradient>
    </defs>
    <rect width="1120" height="540" fill="var(--paper)"/>
    <g role="img" aria-label="Photo: two women chatting with coffee on a sofa"><rect x="0" y="160" width="373" height="200" fill="url(#sofaRoom)"/></g>
    <g role="img" aria-label="Photo: person meditating by the sea at sunset"><rect x="563" y="0" width="183" height="360" fill="url(#sunsetSea)"/></g>
    <path d="M0,330 Q300,300 560,326 Q850,356 1120,300 L1120,540 L0,540Z" fill="var(--teal)"/>
    <path d="M0,350 Q300,320 560,346 Q850,376 1120,320 L1120,540 L0,540Z" fill="var(--forest)"/>
    <line x1="373" y1="0" x2="373" y2="540" stroke="rgba(0,0,0,.12)"/>
    <line x1="746" y1="0" x2="746" y2="540" stroke="rgba(0,0,0,.12)"/>
  </svg>

  <div class="panel panel--1">
    <h2 class="heading section-title"><span class="tag">Who</span>We Are</h2>
    <p class="body-copy who-copy">Lorem ipsum dolor sit amet, consectetur adipiscing elit, sed do eiusmod tempor incididunt ut labore et dolore magna aliqua. Ut enim ad minim veniam, quis nostrud exercitation ullamco laboris nisi ut aliquip ex ea commodo consequat.</p>
    <div class="step" style="top:402px;left:30px">
      <span class="step-icon"><svg viewBox="0 0 20 20" fill="none" stroke="#fff" stroke-width="1.8"><circle cx="8" cy="8" r="5"/><path d="M12,12 L17,17"/></svg></span>
      <div><p class="step-name">Search</p><p class="step-copy">This is the text area for this paragraph. To change it, simply click here and type</p></div>
    </div>
    <div class="step" style="top:472px;left:30px">
      <span class="step-icon"><svg viewBox="0 0 20 20" fill="none" stroke="#fff" stroke-width="1.8"><rect x="4" y="9" width="12" height="8" rx="1"/><path d="M7,9 V6 a3,3 0 0 1 6,0 V9"/></svg></span>
      <div><p class="step-name">Encrypt</p><p class="step-copy">This is the text area for this paragraph. To change it, simply click here and type</p></div>
    </div>
  </div>

  <div class="panel panel--2">
    <h2 class="heading with-title"><span class="tag">Who</span><br>We<br>Work<br>With</h2>
    <p class="with-copy">Lorem ipsum dolor sit amet, consectetur adipiscing elit, sed do eiusmod tempor incididunt ut labore et dolore magna aliqua. Ut enim ad minim veniam, quis nostrud exercitation ullamco laboris nisi ut aliquip ex ea commodo consequat.</p>
    <div class="step" style="top:402px;left:24px">
      <span class="step-icon"><svg viewBox="0 0 20 20" fill="none" stroke="#fff" stroke-width="1.8"><rect x="3" y="5" width="14" height="11" rx="1"/><path d="M3,9 H17 M8,12 H12"/></svg></span>
      <div><p class="step-name">Organize</p><p class="step-copy">This is the text area for this paragraph. To change it, simply click here and type</p></div>
    </div>
    <div class="step" style="top:472px;left:24px">
      <span class="step-icon"><svg viewBox="0 0 20 20" fill="none" stroke="#fff" stroke-width="1.8"><path d="M5,14 V9 a5,5 0 0 1 10,0 V14 Z M8,17 H12"/></svg></span>
      <div><p class="step-name">Notify</p><p class="step-copy">This is the text area for this paragraph. To change it, simply click here and type</p></div>
    </div>
  </div>

  <div class="panel panel--3">
    <h2 class="heading why-title"><span class="tag">Why</span>Flow States?</h2>
    <p class="body-copy why-copy why-copy--a">Lorem ipsum dolor sit amet, consectetur adipiscing elit, sed do eiusmod tempor incididunt ut labore et dolore magna aliqua. Ut enim ad minim veniam, quis nostrud exercitation ullamco laboris nisi ut aliquip ex ea commodo consequat.</p>
    <p class="body-copy why-copy why-copy--b">Lorem ipsum dolor sit amet, consectetur adipiscing elit, sed do eiusmod tempor incididunt ut labore et dolore magna aliqua. Ut enim ad minim veniam, quis nostrud exercitation ullamco laboris nisi ut aliquip ex ea commodo consequat.</p>
    <div class="brand-mark"></div>
    <div class="step" style="top:392px;left:30px">
      <span class="step-icon"><svg viewBox="0 0 20 20" fill="none" stroke="#fff" stroke-width="1.8"><path d="M4,15 C5,9 9,7 14,7 M11,4 L15,7 L11,10"/></svg></span>
      <div><p class="step-name">Share</p><p class="step-copy">This is the text area for this paragraph. To change it, simply click here and type</p></div>
    </div>
    <div class="step" style="top:462px;left:30px">
      <span class="step-icon"><svg viewBox="0 0 20 20" fill="none" stroke="#fff" stroke-width="1.8"><circle cx="10" cy="10" r="6.5"/><circle cx="10" cy="10" r="2.5"/></svg></span>
      <div><p class="step-name">Target</p><p class="step-copy">This is the text area for this paragraph. To change it, simply click here and type</p></div>
    </div>
  </div>

  <h2 class="band-title">How Does Our Training Work?</h2>
</section>

</body>
</html>
```